User Frontend Design for Support Logging System

I have a PHP web application to manage IT support calls and require a front-end design and user logon screen.

I have attached the current design which needs improving.

I have 2 current designs. The 2nd design is one I have been working on but requires a "professional touch". I also require the tables designed with dummy data from the 1st design.

I have attached my company logo in AI format which I would like incorporated into the design. There should also be a placeholder to supply the users company name upon login.

The screenshots I have attached should explain what I am looking for.

The Home Page should include charts which show statistical information such as:
Number of support tickets logged per month. Bar Chart etc.
Number of currently open support tickets.
Number of Quote Requests awaiting a response.
Number of Files and file repository.
Number of Reports.
Number of Customers.

For the Jobs and Customers pages the table fields should be designed as per the attached screenshots but a better looking tables. The table options such as uploading a file and adding a customer - these options can be changed and displayed differently.

Quotes page should display quotes returned and a "request a quote form".

Files page should have a good structure for browsing through an archive of files.

Profile page should have the option to include a profile picture.

An additional side page should be created for a web based calendar (these calendar entries will be updated by code).

The navbar should also include an alerts section.
The current attached design I have is based on bootstraps navbar.

Inspiration: http://pelvoriad.com/freebie/free-admin-templates-for-backend-panels/

Hopefully this above link will show you some navigation style designs that I am looking for.

Please note, I will be doing the PHP coding myself and it is just the page designs I require in either HTML and or PHP format. I also require the CSS files for this project.
I need the code in a format where I can add and remove items in the menu from the code and not PSD/image based format.

If you think this project requires a higher budget let me know what you would expect and I will increase it!

Any questions, please let me know.
Dummy data can be shown for design purposes.

I have provided you a dummy login to our current system to show you the system:
https://ridge.brivelnetworks.co.uk/
username: dan.prewett@brivelnetworks.co.uk
password:P@55w0rd

```html
<!DOCTYPE html>
<html lang="en">
<head>
<meta charset="utf-8">
<title>Ridge – Call out and support tracker</title>
<link rel="stylesheet" href="https://fonts.googleapis.com/css2?family=Open+Sans:wght@400;600;700&display=swap">
<style>
:root{
  --blue:#2b80c8;
  --blue-dark:#1f6fb5;
  --blue-bright:#1592d4;
  --footer:#1c7fd0;
  --red:#d9442f;
  --side:#f0f0f0;
  --panel:#f7f7f7;
  --panel-head:#ececec;
  --line:#e2e2e2;
  --grey-head:#7a7a7a;
  --dark-head:#4a4a4a;
  --text:#333;
  --muted:#666;
  --white:#fff;
}
*{box-sizing:border-box;margin:0;padding:0}
html,body{width:741px;height:1200px;overflow:hidden;background:var(--white)}
body{font-family:"Open Sans",Arial,sans-serif;color:var(--text)}
.page{position:relative;width:926px;height:1500px;transform:scale(.8);transform-origin:0 0}
.abs{position:absolute}

/* sidebar */
.sidebar{left:0;top:0;width:187px;height:1500px;background:var(--side)}
.brand{left:0;top:0;width:187px;height:103px;background:var(--white);display:flex;align-items:center;justify-content:center;gap:8px}
.brand-dot{width:14px;height:14px;border-radius:50%;background:var(--blue-dark)}
.brand-name{font-size:20px;font-weight:700;color:#1f3f7a;letter-spacing:.5px}
.nav{left:0;top:103px;width:187px;list-style:none}
.nav li{position:relative;height:44.5px;display:flex;align-items:center;padding-left:21px;font-size:12px;color:#333;border-bottom:1px solid #e4e4e4}
.nav li svg{width:13px;height:13px;margin-right:7px;fill:#222}
.nav li.active{background:var(--blue);color:var(--white);font-style:italic;height:46px;border:0}
.nav li.active svg{fill:var(--white)}
.nav li.active::after{content:"";position:absolute;right:-7px;top:16px;border:7px solid transparent;border-left-color:var(--blue);border-right:0}

/* header */
.header{left:187px;top:0;width:739px;height:103px;background:var(--blue)}
.userbar{left:210px;top:16px;width:528px;height:40px;background:var(--white);border-radius:2px;display:flex;align-items:center}
.avatar{width:26px;height:26px;margin:0 12px 0 10px;background:linear-gradient(135deg,#6b5a49,#2e2620);border-radius:2px}
.welcome{width:139px;font-size:11.5px;font-weight:600;color:#999}
.icon-cell{width:57px;height:40px;border-left:1px solid #e3e3e3;display:flex;align-items:center;justify-content:center}
.icon-cell svg{width:14px;height:14px;fill:#aaa}
.icon-cell.last{border-right:1px solid #e3e3e3}
.search{flex:1;display:flex;justify-content:flex-end;padding-right:14px}
.search svg{width:13px;height:13px}
.logout{left:760px;top:16px;width:95px;height:40px;background:var(--red);color:var(--white);font-size:12px;font-weight:700;display:flex;align-items:center;justify-content:center;border-radius:2px}
.product{left:210px;top:68px;color:var(--white);font-size:19px;font-weight:600}
.product span{font-size:11.5px;font-weight:400;margin-left:6px}
.user-menu{left:709px;top:74px;color:var(--white);font-size:11.5px}
.help{left:832px;top:74px;color:var(--white);font-size:11.5px}

/* panels */
.panel{background:var(--panel);border:1px solid var(--line)}
.panel-title{height:38px;background:var(--panel-head);border-bottom:1px solid var(--line);font-size:11.5px;color:#333;padding:12px 0 0 21px}
.panel-tab{position:relative;height:32px;color:var(--white);font-size:13px;font-weight:700;padding:8px 0 0 14px}
.panel-tab::after{content:"";position:absolute;left:24px;bottom:-6px;border:6px solid transparent;border-top-color:inherit;border-bottom:0}
.tab-grey{background:var(--grey-head);border-color:var(--grey-head)}
.tab-dark{background:var(--dark-head);border-color:var(--dark-head)}

.chart{left:237px;top:126px;width:646px;height:298px}

.tickets{left:237px;top:449px;width:311px;height:279px}
.ticket{position:absolute;left:0;width:309px;height:117px}
.ticket + .ticket{border-top:1px solid var(--line)}
.ticket-art{position:absolute;left:19px;top:22px;width:88px;height:68px;border:1px solid #ddd}
.art-a{background:linear-gradient(160deg,#e9f1fa,#c7dbee)}
.art-b{background:linear-gradient(160deg,#f3f3f3,#c9ccd0)}
.ticket-title{position:absolute;left:124px;top:24px;font-size:11px;color:#222}
.ticket-since{position:absolute;left:124px;top:46px;font-size:8.5px;color:#222}
.ticket-body{position:absolute;left:124px;top:64px;width:176px;font-size:8px;line-height:15.5px;color:#333}

.quotes{left:573px;top:449px;width:310px;height:279px}
.field{position:absolute;left:22px;width:265px;height:24px;background:#ececec;font-size:10px;font-weight:600;color:#c4c4c4;padding:5px 0 0 25px}
.send{position:absolute;left:235px;top:240px;width:51px;height:24px;background:var(--blue-dark);color:var(--white);font-size:10px;font-weight:700;display:flex;align-items:center;justify-content:center;border-radius:3px}

.files{left:237px;top:750px;width:646px;height:358px}
.file-table{position:absolute;left:10px;top:55px;border-collapse:collapse;background:var(--white);font-size:10.5px}
.file-table th,.file-table td{border:1px solid #ddd;text-align:center;color:#555;font-weight:400}
.file-table th{height:37px;color:#333;font-size:11px}
.file-table tr.r1 td{border-top:0;height:47px}
.file-table td{height:47px}
.btn{position:absolute;top:304px;width:83px;height:30px;color:var(--white);font-size:11px;display:flex;align-items:center;justify-content:center}
.btn-delete{left:11px;background:#2c2c2c}
.btn-create{left:111px;background:var(--blue-bright)}

.reports{left:237px;top:1133px;width:311px;height:279px}
.reports p{position:absolute;left:16px;top:47px;width:285px;font-size:14px;line-height:32px;color:#222}

.customers{left:573px;top:1133px;width:310px;height:279px}
.person{position:absolute;left:22px;width:280px;height:100px}
.portrait{position:absolute;left:0;top:0;width:58px;height:58px;border-radius:50%;border:2px solid #333;background:linear-gradient(135deg,#e7e2dc,#c5b8ab)}
.portrait.green{border-color:#e5e5e5;border-top-color:#2dba6a;border-right-color:#2dba6a}
.person h4{position:absolute;left:76px;top:5px;font-size:13px;font-weight:400;color:#666}
.person .by{position:absolute;left:76px;top:26px;font-size:10px;color:#444}
.person .note{position:absolute;left:76px;top:47px;width:198px;font-size:8px;line-height:15.5px;color:#555}

/* footer */
.footer{left:187px;top:1446px;width:739px;height:54px;background:var(--footer)}
.copyright{left:237px;top:1466px;font-size:10px;color:var(--white)}
.social{left:782px;top:1465px;display:flex;gap:7px}
.social span{width:18px;height:18px;border-radius:50%;background:var(--white)}
</style>
</head>
<body>
<div class="page">

  <aside class="abs sidebar"></aside>
  <div class="abs brand"><span class="brand-dot"></span><span class="brand-name">BRIVEL</span></div>
  <ul class="abs nav">
    <li class="active"><svg viewBox="0 0 16 16"><path d="M8 1 0 8h2v7h4v-5h4v5h4V8h2z"/></svg>Home</li>
    <li><svg viewBox="0 0 16 16"><path d="M14 2a4 4 0 0 0-5 5L1 15l1 1 8-8a4 4 0 0 0 5-5l-2 2-2-2z"/></svg>Jobs</li>
    <li><svg viewBox="0 0 16 16"><circle cx="8" cy="4" r="3.5"/><path d="M2 16c0-5 2-7 6-7s6 2 6 7z"/></svg>Customers</li>
    <li><svg viewBox="0 0 16 16"><path d="M3 0h10v16H3z"/></svg>Inventory</li>
    <li><svg viewBox="0 0 16 16"><path d="M1 8h3v8H1zM6 3h3v13H6zM11 0h3v10h-3zM11 12h3v4h-3z"/></svg>Reports</li>
    <li><svg viewBox="0 0 16 16"><path d="M3 0h7l3 3v13H3z"/></svg>Files</li>
    <li><svg viewBox="0 0 16 16"><ellipse cx="8" cy="7" rx="7" ry="6"/><path d="M3 11 2 16l5-3z"/></svg>Quotes</li>
  </ul>

  <header class="abs header"></header>
  <div class="abs userbar">
    <div class="avatar" role="img" aria-label="User profile photo"></div>
    <div class="welcome">Welcome, Tomas</div>
    <div class="icon-cell"><svg viewBox="0 0 16 16"><path d="M1 3h14v10H1z M1 3l7 6 7-6" fill="none" stroke="#aaa" stroke-width="1.6"/></svg></div>
    <div class="icon-cell"><svg viewBox="0 0 16 16"><path d="M8 1c3 0 4 2 4 5v4l2 2H2l2-2V6c0-3 1-5 4-5zM6 14h4a2 2 0 0 1-4 0z"/></svg></div>
    <div class="icon-cell last"><svg viewBox="0 0 16 16"><circle cx="8" cy="8" r="5" fill="none" stroke="#aaa" stroke-width="3" stroke-dasharray="2.2 1.7"/><circle cx="8" cy="8" r="2"/></svg></div>
    <div class="search"><svg viewBox="0 0 16 16"><circle cx="6.5" cy="6.5" r="4.5" fill="none" stroke="#aaa" stroke-width="2"/><path d="M10 10l5 5" stroke="#aaa" stroke-width="2.4"/></svg></div>
  </div>
  <div class="abs logout">LOGOUT</div>
  <div class="abs product">Ridge |<span>Call out and support tracker</span></div>
  <div class="abs user-menu">Owen Harcastle &#9660;</div>
  <div class="abs help">Help</div>

  <section class="abs panel chart">
    <div class="panel-title">Support tickets logged per month Bar Chart etc.</div>
    <svg class="abs" style="left:-1px;top:-1px" width="646" height="298" viewBox="237 126 646 298" font-family="Open Sans, Arial, sans-serif">
      <g stroke="#e3e3e3" stroke-width="1">
        <line x1="282" y1="187" x2="882" y2="187"/>
        <line x1="282" y1="237" x2="882" y2="237"/>
        <line x1="282" y1="287" x2="882" y2="287"/>
        <line x1="282" y1="337" x2="882" y2="337"/>
        <line x1="282" y1="387" x2="882" y2="387"/>
      </g>
      <g font-size="9" fill="#666" text-anchor="end">
        <text x="272" y="190">2,000</text><text x="272" y="240">1,500</text>
        <text x="272" y="290">1,000</text><text x="272" y="340">500</text><text x="272" y="390">0</text>
      </g>
      <path fill="#2a74bb" d="M282 387V307L310 309 338 305 367 303 395 308 423 301 452 308 480 219 508 235 537 245 565 299 593 298 622 304 650 302 678 300 707 281 735 268 764 265 792 254 820 254 848 263 878 268V387Z"/>
      <polyline fill="none" stroke="#1d5f9f" stroke-width="1.5" points="282,307 310,309 338,305 367,303 395,308 423,301 452,308 480,219 508,235 537,245 565,299 593,298 622,304 650,302 678,300 707,281 735,268 764,265 792,254 820,254 848,263 878,268"/>
      <g fill="#fff" stroke="#1d5f9f" stroke-width="1.2">
        <circle cx="282" cy="307" r="2.6"/><circle cx="310" cy="309" r="2.6"/><circle cx="338" cy="305" r="2.6"/><circle cx="367" cy="303" r="2.6"/>
        <circle cx="395" cy="308" r="2.6"/><circle cx="423" cy="301" r="2.6"/><circle cx="452" cy="308" r="2.6"/><circle cx="480" cy="219" r="2.6"/>
        <circle cx="508" cy="235" r="2.6"/><circle cx="565" cy="299" r="2.6"/><circle cx="593" cy="298" r="2.6"/><circle cx="622" cy="304" r="2.6"/>
        <circle cx="650" cy="302" r="2.6"/><circle cx="678" cy="300" r="2.6"/><circle cx="707" cy="281" r="2.6"/><circle cx="735" cy="268" r="2.6"/>
        <circle cx="764" cy="265" r="2.6"/><circle cx="792" cy="254" r="2.6"/><circle cx="820" cy="254" r="2.6"/><circle cx="848" cy="263" r="2.6"/>
        <circle cx="878" cy="268" r="2.6"/>
      </g>
      <circle cx="537" cy="245" r="4.5" fill="#1d5f9f" stroke="#fff" stroke-width="1.5"/>
      <rect x="507" y="199" width="58" height="35" rx="4" fill="#fff" fill-opacity=".92" stroke="#ddd"/>
      <text x="514" y="213" font-size="8.5" font-weight="700" fill="#333">2012-10-10</text>
      <text x="514" y="227" font-size="8.5" fill="#1d5f9f">Visits: 1,420</text>
      <g font-size="9" fill="#666" text-anchor="middle">
        <text x="338" y="405">2012-10-03</text><text x="423" y="405">2012-10-06</text><text x="508" y="405">2012-10-09</text>
        <text x="593" y="405">2012-10-12</text><text x="678" y="405">2012-10-15</text><text x="764" y="405">2012-10-18</text>
        <text x="848" y="405">2012-10-21</text>
      </g>
    </svg>
  </section>

  <section class="abs panel tickets">
    <div class="panel-tab tab-grey">Currently open support tickets</div>
    <div class="ticket" style="top:33px">
      <div class="ticket-art art-a" role="img" aria-label="Illustration of a coloured 3D bar chart"></div>
      <div class="ticket-title">Curabitur bibendum ornare dolor</div>
      <div class="ticket-since">Since: 17/05/2012</div>
      <div class="ticket-body">Lorem ipsum dolor sit amet, consectetur adipi-scing elit. Curabitur bibendum ornare dolor, quis ullamcorper ligula sodales at. Nulla tellus elit,</div>
    </div>
    <div class="ticket" style="top:150px">
      <div class="ticket-art art-b" role="img" aria-label="Illustration of a rising 3D bar chart with arrow"></div>
      <div class="ticket-title">Curabitur bibendum ornare dolor</div>
      <div class="ticket-since">Since: 17/05/2012</div>
      <div class="ticket-body">Lorem ipsum dolor sit amet, consectetur adipi-scing elit. Curabitur bibendum ornare dolor, quis ullamcorper ligula sodales at. Nulla tellus elit,</div>
    </div>
  </section>

  <section class="abs panel quotes">
    <div class="panel-tab tab-dark">Quote Requests awaiting a response</div>
    <div class="field" style="top:61px">Name</div>
    <div class="field" style="top:102px">Phone</div>
    <div class="field" style="top:141px">Email</div>
    <div class="field" style="top:180px;height:46px">Comments</div>
    <div class="send">SEND</div>
  </section>

  <section class="abs panel files">
    <div class="panel-title">Files and file repository</div>
    <table class="file-table">
      <colgroup><col style="width:85px"><col style="width:80px"><col style="width:79px"><col style="width:86px"><col style="width:103px"><col style="width:106px"><col style="width:76px"></colgroup>
      <tr><th>Data1</th><th>Data2</th><th>Data3</th><th>Data 4</th><th>Data 5</th><th>Data 6</th><th>Data6</th></tr>
      <tr class="r1"><td>Data</td><td>Data</td><td>Data</td><td>Data</td><td>Data</td><td>Data</td><td>Data</td></tr>
      <tr><td>Data</td><td>Data</td><td>Data</td><td>Data</td><td>Data</td><td>Data</td><td>Data</td></tr>
      <tr><td style="height:44px">Data</td><td>Data</td><td>Data</td><td>Data</td><td>Data</td><td>Data</td><td>Data</td></tr>
      <tr><td style="height:45px">Data</td><td>Data</td><td>Data</td><td>Data</td><td>Data</td><td>Data</td><td>Data</td></tr>
    </table>
    <div class="btn btn-delete">Delete</div>
    <div class="btn btn-create">Create</div>
  </section>

  <section class="abs panel reports">
    <div class="panel-tab tab-grey">Reports</div>
    <p>A very small degree of hope is sufficient to cause the birth of love.<br>Great Be faithful in small things because it is in them that your strength lies.<br>Better This is one small step for a man, one giant leap for mankind.</p>
  </section>

  <section class="abs panel customers">
    <div class="panel-tab tab-dark">Customers</div>
    <div class="person" style="top:53px">
      <div class="portrait" role="img" aria-label="Customer portrait photo"></div>
      <h4>Half way there!</h4>
      <div class="by">By Rhys</div>
      <div class="note">Lorem ipsum dolor sit amet, conse adipiscing. dolor sit amet, conse adip. ipsum dolor sit amet, conse adipiscing. dolor sit amet, conse adip.</div>
    </div>
    <div class="person" style="top:160px">
      <div class="portrait green" role="img" aria-label="Customer portrait photo"></div>
      <h4>Half way there!</h4>
      <div class="by">By Rhys</div>
      <div class="note">Lorem ipsum dolor sit amet, conse adipiscing. dolor sit amet, conse adip. ipsum dolor sit amet, conse adipiscing. dolor sit amet, conse adip.</div>
    </div>
  </section>

  <footer class="abs footer"></footer>
  <div class="abs copyright">Copyrights@2014 Brivel. All Right Reserved.</div>
  <div class="abs social"><span></span><span></span><span></span><span></span></div>

</div>
</body>
</html>
```